Company Business Card, for Harborveldt.com Floating homes and Marinas

To design a new great looking business card that follows some how the theme of our business and website. Harborveldt.com

I have attached our logo and a copy of our existing card (boring)

   We appreciate everyones efforts so far there are some very interesting designs. We are thinking that our company is more than just a Marina manufacturer, we build many different floating products and we would like our card to show case those products. There has been one card that has done this, and we are leaning towards that design. We prefer that our logo and company name are proportional on the card, and our mission statement be also shown. Thank you                                

                                   

 We do like your designs, on the back of the card  we want to show all 6 different product types as shown on the front of our website.

                                   

Sorry some designers have the images on the front, and that is okay as well. We just want on the card all 6 areas that we manufacture.

• Must have a new look, maybe nautical, following the theme of what our company manufactures.

Logo
Company name: Consolidated Pontoon Dockworks Group, Inc.

Website: www.HarborVeldt.com

Employee name & title

Mission statement: "Craftsmanship is the keel that carries every voyage"

Our Address: 4718 Quillan Avenue, Delta, B.C. Canada, V3K 2R7

• Colour and unique presentation,

```html
<!DOCTYPE html>
<html lang="en">
<head>
<meta charset="utf-8">
<title>Consolidated Pontoon Dockworks Group – Business Card</title>
<link rel="stylesheet" href="https://fonts.googleapis.com/css2?family=Jost:wght@400;500&display=swap">
<style>
  :root {
    --page: #ffffff;
    --card: #000000;
    --ink: #ffffff;
    --brand-red: #b5141d;
    --steel-dark: #6c747c;
    --steel-mid: #9ba1a7;
    --steel-light: #f5f5f5;
  }
  * { margin: 0; padding: 0; box-sizing: border-box; }
  html, body {
    width: 1200px;
    height: 900px;
    overflow: hidden;
    background: var(--page);
  }
  .sheet {
    position: absolute;
    left: 0;
    top: 0;
    width: 1280px;
    height: 960px;
    transform: scale(0.9375);
    transform-origin: 0 0;
    font-family: "Jost", "Futura", sans-serif;
    color: var(--ink);
  }
  .card {
    position: absolute;
    width: 600px;
    height: 360px;
    background: var(--card);
    overflow: hidden;
  }
  .card--front { left: 208px; top: 87px; }
  .card--back  { left: 416px; top: 511px; }

  .steel-band {
    position: absolute;
    left: 0;
    width: 100%;
    height: 14px;
    background: linear-gradient(90deg,
      var(--steel-dark) 0%,
      var(--steel-mid) 22%,
      var(--steel-light) 40%,
      var(--steel-mid) 55%,
      var(--steel-dark) 75%,
      var(--steel-mid) 88%,
      var(--steel-dark) 100%);
  }
  .accent-line {
    position: absolute;
    left: 0;
    width: 100%;
    height: 3px;
    background: var(--brand-red);
  }

  /* Front */
  .front-rule { position: absolute; left: 0; top: 73px; width: 100%; height: 18px; }
  .front-rule .accent-line { top: 0; }
  .front-rule .steel-band { top: 3px; }
  .brand-gap {
    position: absolute;
    left: 220px;
    top: 38px;
    width: 161px;
    height: 105px;
    background: var(--card);
    display: flex;
    align-items: center;
    justify-content: center;
  }
  .brand-name {
    font-size: 44px;
    font-weight: 500;
    letter-spacing: 2px;
    color: var(--ink);
  }
  .person-name {
    position: absolute;
    top: 176px;
    width: 100%;
    text-align: center;
    font-size: 40px;
    font-weight: 400;
    letter-spacing: 0.5px;
  }
  .person-title {
    position: absolute;
    top: 229px;
    width: 100%;
    text-align: center;
    font-size: 18px;
  }
  .mission {
    position: absolute;
    top: 285px;
    width: 100%;
    text-align: center;
    font-size: 18px;
  }
  .front-bottom { top: 321px; }

  /* Back */
  .back-top { top: 30px; }
  .company-mark {
    position: absolute;
    top: 58px;
    width: 100%;
    text-align: center;
    font-size: 42px;
    font-weight: 400;
  }
  .company-line {
    position: absolute;
    width: 100%;
    text-align: center;
    font-size: 18px;
  }
  .company-line--name { top: 133px; }
  .company-line--address { top: 166px; }
  .contact-panel {
    position: absolute;
    left: 0;
    top: 216px;
    width: 100%;
    height: 100px;
    background: var(--brand-red);
    display: flex;
    flex-direction: column;
    align-items: center;
    justify-content: center;
    font-size: 24px;
    line-height: 34px;
  }
  .back-bottom { top: 320px; }
</style>
</head>
<body>
  <main class="sheet">
    <section class="card card--front" aria-label="Business card front">
      <div class="front-rule">
        <div class="accent-line"></div>
        <div class="steel-band"></div>
      </div>
      <div class="brand-gap"><span class="brand-name">CPDG</span></div>
      <h1 class="person-name">EDVIN LARSHOLT</h1>
      <p class="person-title">Senior Project Manager</p>
      <p class="mission">Craftsmanship is the keel that carries every voyage</p>
      <div class="steel-band front-bottom"></div>
    </section>

    <section class="card card--back" aria-label="Business card back">
      <div class="steel-band back-top"></div>
      <h2 class="company-mark">CPDG</h2>
      <p class="company-line company-line--name">Consolidated Pontoon Dockworks Group, Inc.</p>
      <p class="company-line company-line--address">4718 Quillan Avenue, Delta, B.C. Canada, V3K 2R7</p>
      <div class="contact-panel">
        <span class="contact-web">www.HarborVeldt.com</span>
        <span class="contact-email">edvin@HarborVeldt.com</span>
      </div>
      <div class="steel-band back-bottom"></div>
    </section>
  </main>
</body>
</html>
```